Einladungskarten Design
Zielgruppe
Die Zielgruppe besteht aus allen Privatpersonen, die eine Feier planen und auf der Suche nach individuellen, professionell gestalteten Einladungskarten für Ihre Feier sind:
Hochzeit
Geburtstag (meistens runde Geburtstage)
Mottoparty´s
Danksagung zur Gebur
Aufgabenstellung
Für das Online-Angebot www.festbogen-kartenhaus.de werden kreative Vorschläge für Einladungskarten und Danksagungskarten in verschiedenen Kategorien gesucht: Hochzeit, Geburtstag, Party, Mottoparty, Geburt und weitere Themen. Das Thema ist wählbar, da für alle Kategorien neue, frische Entwürfe benötigt werden.
Dies ist kein Wettbewerb im herkömmlichen Sinne, da es keinen einzelnen Gewinner gibt. Jeder Kartenentwurf, der für das Online Angebot ausgewählt wird, wird mit 100,00 Eur honoriert.
Voraussetzung für die Honorarzahlung ist das Einverständnis der Veröffentlichung und die Übertragung der Nutzungsrechte.

```html
<!DOCTYPE html>
<html lang="de">
<head>
<meta charset="utf-8">
<title>Für immer – Tina &amp; Klaus</title>
<link rel="stylesheet" href="https://fonts.googleapis.com/css2?family=Josefin+Sans:wght@100;200&display=swap">
<style>
  :root {
    --paper: #ffffff;
    --ink: #1b1b1b;
    --olive: #a59b5c;
    --ochre: #a7793e;
    --rust: #a4381f;
  }
  html, body {
    margin: 0;
    padding: 0;
    width: 850px;
    height: 1200px;
    overflow: hidden;
    background: var(--paper);
  }
  .card {
    position: relative;
    width: 850px;
    height: 1200px;
    overflow: hidden;
    background: var(--paper);
    font-family: "Josefin Sans", "Helvetica Neue", sans-serif;
    color: var(--ink);
  }
  .floral {
    position: absolute;
    inset: 0;
    width: 850px;
    height: 1200px;
  }
  .headline {
    position: absolute;
    left: 22px;
    top: 650px;
    margin: 0;
    font-weight: 100;
    font-size: 185px;
    line-height: 0.75;
    letter-spacing: 0.06em;
    white-space: nowrap;
    transform-origin: 0 100%;
    transform: rotate(-45deg);
  }
  .couple {
    position: absolute;
    left: 578px;
    top: 252px;
    margin: 0;
    font-weight: 100;
    font-size: 66px;
    line-height: 78px;
    letter-spacing: 0.05em;
    white-space: nowrap;
    transform-origin: 0 0;
    transform: rotate(45deg);
  }
  .couple span {
    display: block;
  }
  .couple .second {
    padding-left: 91px;
  }
</style>
</head>
<body>
  <main class="card">
    <svg class="floral" viewBox="0 0 850 1200" xmlns="http://www.w3.org/2000/svg">
      <defs>
        <linearGradient id="bloom-tone" x1="0" y1="0" x2="1" y2="1">
          <stop offset="0" stop-color="var(--olive)"/>
          <stop offset="0.5" stop-color="var(--ochre)"/>
          <stop offset="1" stop-color="var(--rust)"/>
        </linearGradient>
        <linearGradient id="bloom-tone-top" x1="0" y1="0" x2="1" y2="1">
          <stop offset="0" stop-color="var(--rust)"/>
          <stop offset="1" stop-color="var(--olive)"/>
        </linearGradient>
      </defs>
      <g role="img" aria-label="Holzschnitt-Illustration einer Pfingstrose mit Blättern, oben links">
        <path d="M0 0 H340 C390 40 380 140 330 200 C290 260 200 300 120 290 C60 282 20 250 0 230 Z" fill="url(#bloom-tone-top)" opacity="0.95"/>
      </g>
      <g role="img" aria-label="Große Holzschnitt-Illustration einer Pfingstrose mit Blättern und Knospen, untere Kartenhälfte">
        <path d="M0 800 C60 760 150 720 230 700 C300 600 420 590 520 630 C600 660 650 720 690 780 C760 800 820 850 850 900 V1200 H0 Z" fill="url(#bloom-tone)" opacity="0.95"/>
      </g>
      <g role="img" aria-label="Blätterzweig am rechten Rand">
        <path d="M850 560 C790 570 720 610 680 660 C700 700 760 740 850 760 Z" fill="url(#bloom-tone)" opacity="0.9"/>
      </g>
    </svg>

    <h1 class="headline">FÜRIMMER</h1>
    <p class="couple"><span>TINA&amp;</span><span class="second">KLAUS</span></p>
  </main>
</body>
</html>
```